Shopify Design for a Head Shop

This will be a Shopify design that sells Delta-8 and other hemp based products. Looking for a 70's psychedelic retro vibe. Something funny and trippy but high brow. Mythical or maybe spiritual but more ironically than anything else. The appeal is going to need to be towards 'stoners' but let's appeal to the 'stoners' that hold decent jobs and have families. 'Stoners' that went to college. The business is called "Bright Fern Vapors". Stick to that 70's psychedelic theme. 70's colors, fonts, and feel. It should be crisp, light hearted, and not cluttered. I have included a bunch of images of just 'stuff' I like to give a better idea of how it should feel. DO NOT use them in the design, please. They are examples. I don't know if these images are under a copyright plus they are low quality. The only usable material uploaded should be my logo.

Target Market(s)

Adults over the age of 21

Industry/Entity Type

Retail

Coding

Coded - Design and coding required

Requirements
Must have
• Must fit in with logo's color scheme. It's uploaded with the filename logo. Age verification. Support 200+ products.
Should not have
• marijuana images

```html
<!DOCTYPE html>
<html lang="en">
<head>
<meta charset="utf-8">
<title>Bright Fern Vapors – Storefront</title>
<link href="https://fonts.googleapis.com/css2?family=Titan+One&family=Raleway:wght@300;400;500&display=swap" rel="stylesheet">
<style>
:root{
  --canvas:#ffffff;
  --cream:#f6ecdc;
  --card:#f9f3e9;
  --red:#d9574a;
  --footer:#eb5b4b;
  --ink:#3b3431;
  --muted:#6b5f59;
  --yellow:#f2c14e;
  --teal:#6f9d9c;
  --rule:#e2d4c1;
  --display:"Titan One", "Arial Black", sans-serif;
  --body:"Raleway", "Helvetica Neue", sans-serif;
}
*{box-sizing:border-box;margin:0;padding:0}
html,body{width:810px;height:1200px;overflow:hidden;background:var(--canvas)}
.board{position:relative;width:810px;height:1200px}
.page{position:absolute;top:25px;width:363px;height:1151px;background:var(--cream);overflow:hidden;font-family:var(--body);color:var(--ink)}
.page--gate{left:28px}
.page--open{left:419px}
.page *{position:absolute}
.page .flow, .page .flow *{position:static}

.announce{left:0;top:0;width:100%;height:12px;background:var(--red);color:#fff;font-size:4px;line-height:12px;text-align:center}
.header{left:0;top:12px;width:100%;height:28px}
.brand{left:35px;top:8px;display:flex;align-items:center;gap:2px}
.brand, .brand *{position:static}
.brand-dot{width:8px;height:8px;border-radius:50%;background:var(--teal)}
.brand-name{font-family:var(--body);font-weight:500;font-size:4px;line-height:4.4px;color:var(--ink);width:22px}
.nav{top:11px;font-size:4.5px;color:var(--muted)}
.icon{top:9px;width:8px;height:8px}

.hero{left:0;top:40px;width:100%;height:143px;background:linear-gradient(115deg,#e16a4d 0%,#f3c45b 22%,#f6e3c2 40%,#79a5a2 58%,#f3c45b 76%,#e16a4d 100%)}
.hero-card{left:34px;top:70px;width:148px;height:91px;background:var(--card);border:1px solid var(--red);border-bottom-width:2px;border-radius:4px}
.hero-kicker{left:9px;top:20px;font-family:var(--display);font-size:8px;color:var(--ink);letter-spacing:.2px}
.hero-title{left:9px;top:35px;font-family:var(--display);font-size:11.2px;color:var(--ink);white-space:nowrap}
.pill{border:1px solid var(--red);border-radius:10px;font-size:5px;text-align:center;color:var(--ink);background:var(--card)}
.hero-cta{left:9px;top:59px;width:49px;height:18px;line-height:16px}
.pager{top:186px;font-size:4.5px;color:var(--muted)}
.rule{left:0;top:197px;width:100%;height:1px;background:var(--rule)}

.section-title{left:34px;font-family:var(--display);font-size:12.5px;color:var(--ink);letter-spacing:.2px}
.product{width:71px;height:72px;border:1px solid var(--red);border-bottom-width:1.5px;border-radius:2px;overflow:hidden;background:var(--card)}
.product-shot{left:22%;top:12%;width:56%;height:76%;border-radius:3px}
.product-name{font-size:5.6px;color:var(--ink)}
.product-price{font-size:5.4px;color:var(--ink)}

.tile{border:1px solid var(--red);border-bottom-width:1.5px;border-radius:1px;overflow:hidden}
.tile-label{font-size:5.4px;color:var(--ink);display:flex;align-items:center;gap:3px}
.tile-label svg{position:static}

.about{left:34px;top:748px;width:295px;height:133px;border:1px solid var(--red);border-bottom-width:1.5px;border-radius:2px;overflow:hidden}
.about-shot{left:0;top:0;width:116px;height:100%;background:linear-gradient(160deg,#cfcac2,#a9a49c 55%,#d8a24a);border-right:1px solid var(--muted)}
.about-title{left:131px;top:24px;font-family:var(--display);font-size:13px}
.about-copy{left:130px;top:45px;width:155px;font-size:4.7px;line-height:9px;color:var(--muted)}
.about-copy p{position:static;margin-bottom:2.5px}

.signup{left:34px;top:898px;width:295px;height:112px;border:1px solid var(--red);border-bottom-width:1.5px;border-radius:2px;text-align:center}
.signup-title{left:0;top:21px;width:100%;font-family:var(--display);font-size:13px}
.signup-copy{left:12px;top:46px;width:270px;font-size:4.9px;line-height:9px;color:var(--muted)}
.signup-field{left:53px;top:73px;width:188px;height:17px;border:1px solid var(--red);border-radius:9px;font-size:5px;line-height:15px;text-align:left;padding-left:12px;color:var(--ink)}

.footer{left:0;top:1028px;width:100%;height:123px;background:var(--footer);color:#fff}
.footer-brand{left:34px;top:22px;display:flex;align-items:center;gap:4px}
.footer-brand, .footer-brand *{position:static}
.footer-dot{width:16px;height:16px;border-radius:50%;background:#fff}
.footer-name{font-family:var(--body);font-weight:500;font-size:8px;line-height:9px;width:40px}
.footer-head{top:15px;font-size:5.6px}
.footer-list{top:26px;font-size:5.2px;line-height:9px}
.footer-list span, .footer-about span{position:static;display:block}
.footer-about{left:216px;top:26px;width:115px;font-size:5.2px;line-height:9px}
.social{top:72px;width:7px;height:7px;border-radius:50%;background:#fff}
.footer-rule{left:34px;top:87px;width:295px;height:.6px;background:rgba(255,255,255,.45)}
.country{left:34px;top:94px;font-size:5px}
.currency{left:34px;top:103px;width:45px;height:13px;border:1px solid rgba(255,255,255,.8);border-radius:2px;font-size:5px;line-height:11px;padding-left:6px}
.currency svg{left:34px;top:4px}
.pay{top:98px;width:9px;height:6px;border-radius:1px;background:#fff}
.legal{right:34px;top:110px;font-size:3.8px}
.edition{left:345px;top:107px;font-size:3.4px}

.scrim{left:0;top:0;width:100%;height:100%;background:rgba(38,32,30,.64)}
.gate{left:107px;top:104px;width:149px;height:91px;background:var(--card);border:1px solid var(--red);border-bottom-width:2px;border-radius:4px;text-align:center}
.gate-title{left:0;top:22px;width:100%;font-family:var(--display);font-size:10.6px;color:var(--ink);white-space:nowrap}
.gate-copy{left:0;top:41px;width:100%;font-size:5px;color:var(--ink)}
.gate-btn{top:61px;width:33px;height:17px;line-height:15px}
.gate-yes{left:38px;background:var(--yellow)}
.gate-no{left:77px}
</style>
</head>
<body>
<div class="board">

  <!-- Storefront with age gate open -->
  <section class="page page--gate">
    <div class="announce">Early birds get exclusive offers</div>
    <header class="header">
      <div class="brand"><span class="brand-dot"></span><span class="brand-name">Bright Fern Vapors</span></div>
      <span class="nav" style="left:69px">Home</span>
      <span class="nav" style="left:90px">Shop</span>
      <span class="nav" style="left:108px">About</span>
      <span class="nav" style="left:128px">Contact</span>
      <svg class="icon" style="left:306px" viewBox="0 0 10 10"><circle cx="4.2" cy="4.2" r="3" fill="none" stroke="#3b3431" stroke-width="1"/><path d="M6.4 6.4L9 9" stroke="#3b3431" stroke-width="1"/></svg>
      <svg class="icon" style="left:321px" viewBox="0 0 10 10"><rect x="1.5" y="2.5" width="7" height="6.5" rx="1" fill="none" stroke="#3b3431" stroke-width="1"/><path d="M3.5 4V2.5a1.5 1.5 0 0 1 3 0V4" fill="none" stroke="#3b3431" stroke-width="1"/></svg>
    </header>
    <div class="hero" role="img" aria-label="Retro 70s swirl of red, yellow, teal and cream rays"></div>
    <div class="hero-card">
      <span class="hero-kicker">WELCOME TO</span>
      <span class="hero-title">BRIGHT FERN VAPORS</span>
      <span class="pill hero-cta">Shop Now</span>
    </div>
    <span class="pager" style="left:165px">&lsaquo;</span>
    <span class="pager" style="left:176px">1/2</span>
    <span class="pager" style="left:195px">&rsaquo;</span>
    <div class="rule"></div>

    <h2 class="section-title" style="top:223px">OUR BESTSELLERS</h2>
    <div class="product" style="left:34px;top:249px"><div class="product-shot" role="img" aria-label="Jar of colourful gummies" style="background:linear-gradient(#e9e2d6,#e7803f 40%,#f1c64a)"></div></div>
    <div class="product" style="left:108px;top:249px"><div class="product-shot" role="img" aria-label="Amber dropper bottle" style="left:38%;width:24%;background:linear-gradient(#efe6d8 20%,#5a2c18 35%,#3a1b10)"></div></div>
    <div class="product" style="left:182px;top:249px"><div class="product-shot" role="img" aria-label="Small bottle of green oil" style="left:32%;width:36%;top:28%;height:56%;background:radial-gradient(#c8c22a,#7d7d10)"></div></div>
    <div class="product" style="left:257px;top:249px"><div class="product-shot" role="img" aria-label="Slim white vape pen" style="left:44%;width:12%;background:linear-gradient(#222 12%,#d9d9d9 13%)"></div></div>
    <span class="product-name" style="left:34px;top:329px">Lorem Ipsum</span><span class="product-price" style="left:34px;top:339px">$50,000</span>
    <span class="product-name" style="left:108px;top:329px">Lorem Ipsum</span><span class="product-price" style="left:108px;top:339px">$50,000</span>
    <span class="product-name" style="left:182px;top:329px">Lorem Ipsum</span><span class="product-price" style="left:182px;top:339px">$50,000</span>
    <span class="product-name" style="left:257px;top:329px">Lorem Ipsum</span><span class="product-price" style="left:257px;top:339px">$50,000</span>

    <div class="product" style="left:34px;top:363px"><div class="product-shot" role="img" aria-label="Pink disposable vape" style="left:42%;width:16%;background:linear-gradient(#222 12%,#e0357f 13%)"></div></div>
    <div class="product" style="left:108px;top:363px"><div class="product-shot" role="img" aria-label="Jar of soft gel capsules" style="top:22%;height:62%;background:radial-gradient(#f2d45a,#b98e20)"></div></div>
    <div class="product" style="left:182px;top:363px"><div class="product-shot" role="img" aria-label="Jar of purple gummies" style="background:linear-gradient(#8a5cc8,#c98bd9 40%,#e9d0e6)"></div></div>
    <div class="product" style="left:257px;top:363px"><div class="product-shot" role="img" aria-label="Amber dropper bottle" style="left:38%;width:24%;background:linear-gradient(#efe6d8 20%,#5a2c18 35%,#3a1b10)"></div></div>
    <span class="product-name" style="left:34px;top:443px">Lorem Ipsum</span><span class="product-price" style="left:34px;top:453px">$50,000</span>
    <span class="product-name" style="left:108px;top:443px">Lorem Ipsum</span><span class="product-price" style="left:108px;top:453px">$50,000</span>
    <span class="product-name" style="left:182px;top:443px">Lorem Ipsum</span><span class="product-price" style="left:182px;top:453px">$50,000</span>
    <span class="product-name" style="left:257px;top:443px">Lorem Ipsum</span><span class="product-price" style="left:257px;top:453px">$50,000</span>

    <h2 class="section-title" style="top:481px">FIND YOUR FAV</h2>
    <div class="tile" role="img" aria-label="Colourful gummy candies on a table" style="left:34px;top:508px;width:98px;height:92px;background:linear-gradient(150deg,#d8d8d4,#e46a4a 50%,#f0c23e)"></div>
    <span class="tile-label" style="left:34px;top:605px">Lorem Ipsum <svg width="9" height="4" viewBox="0 0 9 4"><path d="M0 2H8M6 .5L8 2 6 3.5" fill="none" stroke="#3b3431" stroke-width=".6"/></svg></span>
    <div class="tile" role="img" aria-label="Amber dropper bottle on a wooden block" style="left:34px;top:621px;width:98px;height:92px;background:linear-gradient(100deg,#c28a4a,#f0c77c 60%,#e9b766)"></div>
    <span class="tile-label" style="left:34px;top:719px">Lorem Ipsum <svg width="9" height="4" viewBox="0 0 9 4"><path d="M0 2H8M6 .5L8 2 6 3.5" fill="none" stroke="#3b3431" stroke-width=".6"/></svg></span>
    <div class="tile" role="img" aria-label="Close-up of stacked brownies" style="left:144px;top:508px;width:185px;height:202px;background:radial-gradient(circle at 60% 45%,#6e4028,#3a2218 60%,#8a6b4c)"></div>
    <span class="tile-label" style="left:148px;top:718px">Lorem Ipsum <svg width="9" height="4" viewBox="0 0 9 4"><path d="M0 2H8M6 .5L8 2 6 3.5" fill="none" stroke="#3b3431" stroke-width=".6"/></svg></span>

    <div class="about">
      <div class="about-shot" role="img" aria-label="Dropper over a bottle of golden oil with layered colour shadows"></div>
      <h2 class="about-title">ABOUT US</h2>
      <div class="about-copy">
        <p>Lorem ipsum dolor sit amet, consectetur adipiscing elit, sed do eiusmod tempor incididunt ut labore et dolore mag aliqua. Quis ipsum suspendisse ultrices gravida. Risus commodo viverragyfc maecenas accumsan lacus vel facilisis.</p>
        <p>Consectetur adipiscing elit, sed do eiusmod tempor incididunt ut labore et dolore mag aliqua. Quis ipsum suspendisse ultrices gravida. Risus commodo viverragyfc maecenas accumsan.</p>
      </div>
    </div>

    <div class="signup">
      <h2 class="signup-title">SPICE UP YOUR INBOX</h2>
      <p class="signup-copy">Lorem ipsum dolor sit amet, consectetur adipiscing elit, sed do eiusmod tempor incididunt ut labore et dolore mag aliqua. Quis ipsum suspendisse ultrices gravida.</p>
      <div class="signup-field">Email</div>
    </div>

    <footer class="footer">
      <div class="footer-brand"><span class="footer-dot"></span><span class="footer-name">Bright Fern Vapors</span></div>
      <span class="footer-head" style="left:121px">Quick Links</span>
      <div class="footer-list" style="left:121px"><span>Home</span><span>Shop</span><span>About</span><span>Contact</span></div>
      <span class="footer-head" style="left:216px">About Fernwood</span>
      <div class="footer-about"><span>Sed ut perspiciatis unde omnis iste natus error sit voluptatem accusantium doloremque lauda tium, totam rem aperiam, eaque ipsa.</span></div>
      <span class="social" style="left:158px"></span><span class="social" style="left:175px"></span><span class="social" style="left:191px"></span><span class="social" style="left:208px"></span>
      <div class="footer-rule"></div>
      <span class="country">Country</span>
      <div class="currency">USA $<svg width="5" height="3" viewBox="0 0 5 3"><path d="M.5 .5L2.5 2.5 4.5 .5" fill="none" stroke="#fff" stroke-width=".6"/></svg></div>
      <span class="pay" style="left:258px"></span><span class="pay" style="left:270px"></span><span class="pay" style="left:283px"></span><span class="pay" style="left:295px"></span><span class="pay" style="left:308px"></span><span class="pay" style="left:320px"></span>
      <span class="legal">2023 Bright Fern Vapors. All Rights Reserved.</span>
      <span class="edition">C50</span>
    </footer>

    <div class="scrim"></div>
    <div class="gate" role="dialog" aria-label="Age verification">
      <h2 class="gate-title">BRIGHT FERN VAPORS</h2>
      <p class="gate-copy">You must be 18+ to view this paege</p>
      <span class="pill gate-btn gate-yes">Yes</span>
      <span class="pill gate-btn gate-no">No</span>
    </div>
  </section>

  <!-- Storefront after entry -->
  <section class="page page--open">
    <div class="announce">Early birds get exclusive offers</div>
    <header class="header">
      <div class="brand"><span class="brand-dot"></span><span class="brand-name">Bright Fern Vapors</span></div>
      <span class="nav" style="left:69px">Home</span>
      <span class="nav" style="left:90px">Shop</span>
      <span class="nav" style="left:108px">About</span>
      <span class="nav" style="left:128px">Contact</span>
      <svg class="icon" style="left:306px" viewBox="0 0 10 10"><circle cx="4.2" cy="4.2" r="3" fill="none" stroke="#3b3431" stroke-width="1"/><path d="M6.4 6.4L9 9" stroke="#3b3431" stroke-width="1"/></svg>
      <svg class="icon" style="left:321px" viewBox="0 0 10 10"><rect x="1.5" y="2.5" width="7" height="6.5" rx="1" fill="none" stroke="#3b3431" stroke-width="1"/><path d="M3.5 4V2.5a1.5 1.5 0 0 1 3 0V4" fill="none" stroke="#3b3431" stroke-width="1"/></svg>
    </header>
    <div class="hero" role="img" aria-label="Retro 70s swirl of red, yellow, teal and cream rays"></div>
    <div class="hero-card">
      <span class="hero-kicker">WELCOME TO</span>
      <span class="hero-title">BRIGHT FERN VAPORS</span>
      <span class="pill hero-cta">Shop Now</span>
    </div>
    <span class="pager" style="left:165px">&lsaquo;</span>
    <span class="pager" style="left:176px">1/2</span>
    <span class="pager" style="left:195px">&rsaquo;</span>
    <div class="rule"></div>

    <h2 class="section-title" style="top:223px">OUR BESTSELLERS</h2>
    <div class="product" style="left:34px;top:249px"><div class="product-shot" role="img" aria-label="Jar of colourful gummies" style="background:linear-gradient(#e9e2d6,#e7803f 40%,#f1c64a)"></div></div>
    <div class="product" style="left:108px;top:249px"><div class="product-shot" role="img" aria-label="Amber dropper bottle" style="left:38%;width:24%;background:linear-gradient(#efe6d8 20%,#5a2c18 35%,#3a1b10)"></div></div>
    <div class="product" style="left:182px;top:249px"><div class="product-shot" role="img" aria-label="Small bottle of green oil" style="left:32%;width:36%;top:28%;height:56%;background:radial-gradient(#c8c22a,#7d7d10)"></div></div>
    <div class="product" style="left:257px;top:249px"><div class="product-shot" role="img" aria-label="Slim white vape pen" style="left:44%;width:12%;background:linear-gradient(#222 12%,#d9d9d9 13%)"></div></div>
    <span class="product-name" style="left:34px;top:329px">Lorem Ipsum</span><span class="product-price" style="left:34px;top:339px">$50,000</span>
    <span class="product-name" style="left:108px;top:329px">Lorem Ipsum</span><span class="product-price" style="left:108px;top:339px">$50,000</span>
    <span class="product-name" style="left:182px;top:329px">Lorem Ipsum</span><span class="product-price" style="left:182px;top:339px">$50,000</span>
    <span class="product-name" style="left:257px;top:329px">Lorem Ipsum</span><span class="product-price" style="left:257px;top:339px">$50,000</span>

    <div class="product" style="left:34px;top:363px"><div class="product-shot" role="img" aria-label="Pink disposable vape" style="left:42%;width:16%;background:linear-gradient(#222 12%,#e0357f 13%)"></div></div>
    <div class="product" style="left:108px;top:363px"><div class="product-shot" role="img" aria-label="Jar of soft gel capsules" style="top:22%;height:62%;background:radial-gradient(#f2d45a,#b98e20)"></div></div>
    <div class="product" style="left:182px;top:363px"><div class="product-shot" role="img" aria-label="Jar of purple gummies" style="background:linear-gradient(#8a5cc8,#c98bd9 40%,#e9d0e6)"></div></div>
    <div class="product" style="left:257px;top:363px"><div class="product-shot" role="img" aria-label="Amber dropper bottle" style="left:38%;width:24%;background:linear-gradient(#efe6d8 20%,#5a2c18 35%,#3a1b10)"></div></div>
    <span class="product-name" style="left:34px;top:443px">Lorem Ipsum</span><span class="product-price" style="left:34px;top:453px">$50,000</span>
    <span class="product-name" style="left:108px;top:443px">Lorem Ipsum</span><span class="product-price" style="left:108px;top:453px">$50,000</span>
    <span class="product-name" style="left:182px;top:443px">Lorem Ipsum</span><span class="product-price" style="left:182px;top:453px">$50,000</span>
    <span class="product-name" style="left:257px;top:443px">Lorem Ipsum</span><span class="product-price" style="left:257px;top:453px">$50,000</span>

    <h2 class="section-title" style="top:481px">FIND YOUR FAV</h2>
    <div class="tile" role="img" aria-label="Colourful gummy candies on a table" style="left:34px;top:508px;width:98px;height:92px;background:linear-gradient(150deg,#d8d8d4,#e46a4a 50%,#f0c23e)"></div>
    <span class="tile-label" style="left:34px;top:605px">Lorem Ipsum <svg width="9" height="4" viewBox="0 0 9 4"><path d="M0 2H8M6 .5L8 2 6 3.5" fill="none" stroke="#3b3431" stroke-width=".6"/></svg></span>
    <div class="tile" role="img" aria-label="Amber dropper bottle on a wooden block" style="left:34px;top:621px;width:98px;height:92px;background:linear-gradient(100deg,#c28a4a,#f0c77c 60%,#e9b766)"></div>
    <span class="tile-label" style="left:34px;top:719px">Lorem Ipsum <svg width="9" height="4" viewBox="0 0 9 4"><path d="M0 2H8M6 .5L8 2 6 3.5" fill="none" stroke="#3b3431" stroke-width=".6"/></svg></span>
    <div class="tile" role="img" aria-label="Close-up of stacked brownies" style="left:144px;top:508px;width:185px;height:202px;background:radial-gradient(circle at 60% 45%,#6e4028,#3a2218 60%,#8a6b4c)"></div>
    <span class="tile-label" style="left:148px;top:718px">Lorem Ipsum <svg width="9" height="4" viewBox="0 0 9 4"><path d="M0 2H8M6 .5L8 2 6 3.5" fill="none" stroke="#3b3431" stroke-width=".6"/></svg></span>

    <div class="about">
      <div class="about-shot" role="img" aria-label="Dropper over a bottle of golden oil with layered colour shadows"></div>
      <h2 class="about-title">ABOUT US</h2>
      <div class="about-copy">
        <p>Lorem ipsum dolor sit amet, consectetur adipiscing elit, sed do eiusmod tempor incididunt ut labore et dolore mag aliqua. Quis ipsum suspendisse ultrices gravida. Risus commodo viverragyfc maecenas accumsan lacus vel facilisis.</p>
        <p>Consectetur adipiscing elit, sed do eiusmod tempor incididunt ut labore et dolore mag aliqua. Quis ipsum suspendisse ultrices gravida. Risus commodo viverragyfc maecenas accumsan.</p>
      </div>
    </div>

    <div class="signup">
      <h2 class="signup-title">SPICE UP YOUR INBOX</h2>
      <p class="signup-copy">Lorem ipsum dolor sit amet, consectetur adipiscing elit, sed do eiusmod tempor incididunt ut labore et dolore mag aliqua. Quis ipsum suspendisse ultrices gravida.</p>
      <div class="signup-field">Email</div>
    </div>

    <footer class="footer">
      <div class="footer-brand"><span class="footer-dot"></span><span class="footer-name">Bright Fern Vapors</span></div>
      <span class="footer-head" style="left:121px">Quick Links</span>
      <div class="footer-list" style="left:121px"><span>Home</span><span>Shop</span><span>About</span><span>Contact</span></div>
      <span class="footer-head" style="left:216px">About Fernwood</span>
      <div class="footer-about"><span>Sed ut perspiciatis unde omnis iste natus error sit voluptatem accusantium doloremque lauda tium, totam rem aperiam, eaque ipsa.</span></div>
      <span class="social" style="left:158px"></span><span class="social" style="left:175px"></span><span class="social" style="left:191px"></span><span class="social" style="left:208px"></span>
      <div class="footer-rule"></div>
      <span class="country">Country</span>
      <div class="currency">USA $<svg width="5" height="3" viewBox="0 0 5 3"><path d="M.5 .5L2.5 2.5 4.5 .5" fill="none" stroke="#fff" stroke-width=".6"/></svg></div>
      <span class="pay" style="left:258px"></span><span class="pay" style="left:270px"></span><span class="pay" style="left:283px"></span><span class="pay" style="left:295px"></span><span class="pay" style="left:308px"></span><span class="pay" style="left:320px"></span>
      <span class="legal">2023 Bright Fern Vapors. All Rights Reserved.</span>
      <span class="edition">C50</span>
    </footer>
  </section>

</div>
</body>
</html>
```